Orchard of Veloria - Digital Party Invite

I'm throwing a Halloween party with the theme "Orchard of Veloria". The invite will be sent via Quillbright Mail. I need a custom design for the invite. Here are the details:
The image needs to be 670x970.
Needs to be sexy - maybe with Adam & Eve, and the snake w/the apple, etc
Text should be:
You Are Invited To
The Orchard of Veloria
Sat Oct 26 7:00PM
at
Marta & Lucio's Home
527 Harlow Crest Rd 7B
Costumes Highly Encouraged
Adults Only Please

```html
<!DOCTYPE html>
<html lang="en">
<head>
<meta charset="utf-8">
<title>Orchard of Veloria – Party Invite</title>
<link rel="stylesheet" href="https://fonts.googleapis.com/css2?family=Bebas+Neue&family=Oswald:wght@400&family=Playfair+Display:wght@400;500&display=swap">
<style>
  :root {
    --page: #ece7de;
    --card-brown: #3e2516;
    --photo-top: #a58a62;
    --photo-mid: #7d6140;
    --photo-low: #5a3f27;
    --gold: #c9a55a;
    --gold-light: #fff3d6;
    --gold-deep: #d9a95b;
    --white: #ffffff;
    --red: #ec1c24;
  }
  * { margin: 0; padding: 0; box-sizing: border-box; }
  html, body { width: 1200px; height: 1200px; overflow: hidden; }
  body { background: var(--page); position: relative; }

  .invite {
    position: absolute;
    left: 213px; top: 40px;
    width: 774px; height: 1120px;
    background: var(--card-brown);
    overflow: hidden;
  }
  .invite__photo {
    position: absolute; left: 0; top: 0;
    width: 100%; height: 900px;
    background:
      radial-gradient(ellipse at 50% 40%, rgba(200,170,120,0.55), rgba(0,0,0,0) 60%),
      linear-gradient(180deg, var(--photo-top) 0%, var(--photo-mid) 55%, var(--photo-low) 80%, var(--card-brown) 100%);
  }
  .frame {
    position: absolute;
    border: 2px solid var(--gold);
  }
  .frame--outer { left: 42px; top: 38px; width: 688px; height: 1042px; border-width: 3px; }
  .frame--inner { left: 56px; top: 53px; width: 661px; height: 1013px; border-width: 1px; }

  .invited {
    position: absolute; left: 0; width: 100%; top: 258px;
    text-align: center;
    font-family: 'Playfair Display', serif;
    font-size: 25px; line-height: 29px;
    color: var(--white);
  }
  .title {
    position: absolute; left: 0; width: 100%;
    text-align: center;
    font-family: 'Playfair Display', serif;
    font-weight: 400;
    line-height: 1;
    background: linear-gradient(180deg, var(--gold-light) 0%, var(--white) 35%, var(--gold-deep) 100%);
    -webkit-background-clip: text; background-clip: text;
    color: transparent;
  }
  .title--the { top: 380px; font-size: 124px; }
  .title--orchard { top: 496px; font-size: 104px; }
  .title--of { top: 610px; font-size: 124px; }
  .title--veloria { top: 732px; font-size: 104px; }

  .details { position: absolute; top: 882px; left: 0; width: 100%; height: 142px; }
  .details__divider {
    position: absolute; left: 386px; top: 0; width: 1px; height: 142px; background: var(--white);
  }
  .details__col {
    position: absolute; top: 10px; width: 320px; text-align: center;
    color: var(--white); font-family: 'Bebas Neue', sans-serif;
  }
  .details__col--when { left: 58px; }
  .details__col--notes { left: 392px; }
  .details__day { font-size: 30px; line-height: 30px; }
  .details__datetime { font-size: 44px; line-height: 48px; margin-top: 6px; }
  .details__datetime .sep { display: inline-block; width: 1px; height: 32px; background: var(--white); margin: 0 18px; vertical-align: -2px; }
  .details__address { font-family: 'Oswald', sans-serif; font-size: 15px; line-height: 20px; letter-spacing: 0.5px; margin-top: 4px; }
  .details__note { font-size: 30px; line-height: 34px; }
  .adults-badge {
    display: inline-block; margin-top: 10px;
    width: 201px; height: 51px; line-height: 54px;
    background: var(--red); font-size: 36px;
  }
</style>
</head>
<body>
  <main class="invite">
    <div class="invite__photo" role="img" aria-label="Painterly photo of a couple in Eden-style costumes facing each other among fig leaves"></div>
    <div class="frame frame--outer"></div>
    <div class="frame frame--inner"></div>

    <p class="invited">You<br>Are<br>Invited<br>To</p>
    <h1>
      <span class="title title--the">THE</span>
      <span class="title title--orchard">ORCHARD</span>
      <span class="title title--of">OF</span>
      <span class="title title--veloria">VELORIA</span>
    </h1>

    <section class="details">
      <div class="details__col details__col--when">
        <p class="details__day">SATURDAY</p>
        <p class="details__datetime">OCT 26<span class="sep"></span>7:00PM</p>
        <p class="details__address">MARTA &amp; LUCIO’S HOME<br>527 HARLOW CREST RD 7B</p>
      </div>
      <div class="details__divider"></div>
      <div class="details__col details__col--notes">
        <p class="details__note">COSTUMES<br>HIGHLY ENCOURAGED</p>
        <p class="adults-badge">ADULTS ONLY</p>
      </div>
    </section>
  </main>
</body>
</html>
```